Carpet cleaning company focused on high quality needs business cards

We are a growing company that just merged with another company and need to design a new business card. We do both residential as well as commercial cleaning. We do carpet, tile & grout, upholstery, hard floors, and stain & pet odor removal. We treat our customers like family and strive to achieve outstanding results with every job.

```html
<!DOCTYPE html>
<html lang="en">
<head>
<meta charset="utf-8">
<title>Ray's Fresh Crew Cleaning — Business Card</title>
<link href="https://fonts.googleapis.com/css2?family=Montserrat:wght@400;500;700;800&display=swap" rel="stylesheet">
<style>
  :root {
    --brand-red: #ec4a43;
    --ink: #231f20;
    --paper: #ffffff;
    --stage: #2a2a2d;
    --muted-red: #f6d5d3;
  }
  * { box-sizing: border-box; margin: 0; padding: 0; }
  html, body { width: 1200px; height: 900px; overflow: hidden; }
  body {
    background: var(--stage);
    font-family: 'Montserrat', sans-serif;
    display: flex;
    flex-direction: column;
    align-items: center;
    justify-content: center;
    gap: 56px;
  }
  .card {
    position: relative;
    width: 700px;
    height: 400px;
    border-radius: 22px;
    overflow: hidden;
  }
  /* Front */
  .card-front {
    background: var(--brand-red);
    display: flex;
    align-items: center;
    justify-content: center;
    gap: 22px;
  }
  .brand-mark { display: flex; align-items: center; gap: 16px; }
  .brand-square { width: 40px; height: 40px; background: var(--ink); }
  .brand-name {
    font-weight: 800;
    color: var(--ink);
    line-height: 1.02;
    text-transform: uppercase;
  }
  .card-front .brand-name { font-size: 34px; }
  .mascot-area {
    width: 190px; height: 150px;
    background: radial-gradient(ellipse at center, #d9443e 0%, var(--brand-red) 75%);
    border-radius: 8px;
  }

  /* Back */
  .card-back { background: var(--paper); }
  .back-logo {
    position: absolute; left: 34px; top: 34px;
    display: flex; align-items: center; gap: 12px;
  }
  .back-logo .brand-square { width: 30px; height: 30px; background: var(--brand-red); }
  .back-logo .brand-name { font-size: 18px; }
  .faint-mark {
    position: absolute; right: 40px; top: 22px;
    width: 150px; height: 120px;
    background: linear-gradient(135deg, #f7f7f9, #fdf1ef);
    border-radius: 6px;
  }
  .holder {
    position: absolute; left: 34px; top: 118px;
  }
  .holder-name {
    color: var(--brand-red);
    font-weight: 700;
    font-size: 30px;
    letter-spacing: 0.3px;
  }
  .holder-title {
    color: var(--ink);
    font-size: 14px;
    margin-top: 2px;
  }
  .divider {
    position: absolute; left: 34px; right: 40px; top: 186px;
    height: 1.5px; background: var(--brand-red);
  }
  .contact-list {
    position: absolute; left: 34px; top: 202px;
    list-style: none;
    display: flex; flex-direction: column; gap: 6px;
  }
  .contact-list li {
    display: flex; align-items: center; gap: 12px;
    font-size: 14px; color: var(--ink);
  }
  .contact-list svg { width: 14px; height: 14px; fill: var(--brand-red); flex: none; }
  .address {
    position: absolute; right: 40px; top: 222px;
    text-align: right;
    font-size: 14px; color: var(--ink); line-height: 1.35;
  }
  .footer-band { position: absolute; left: 0; bottom: 0; width: 100%; height: 110px; }
  .website-tag {
    position: absolute; right: 30px; bottom: 20px;
    color: var(--paper); font-size: 14px; font-weight: 500;
  }
</style>
</head>
<body>

  <section class="card card-front">
    <div class="mascot-area" role="img" aria-label="Cartoon cleaning technician illustration holding a steam wand"></div>
    <div class="brand-mark">
      <div class="brand-square"></div>
      <div class="brand-name">Ray's<br>Fresh Crew<br>Cleaning</div>
    </div>
  </section>

  <section class="card card-back">
    <div class="back-logo">
      <div class="brand-square"></div>
      <div class="brand-name">Ray's Fresh Crew<br>Cleaning</div>
    </div>
    <div class="faint-mark" role="img" aria-label="Faint decorative background emblem"></div>

    <div class="holder">
      <div class="holder-name">Daniel Moore</div>
      <div class="holder-title">CEO</div>
    </div>
    <div class="divider"></div>

    <ul class="contact-list">
      <li>
        <svg viewBox="0 0 16 16"><path d="M2 5c0-2 2-3 6-3s6 1 6 3l-2 1-1-2H5L4 6 2 5zM3 8h10l1 6H2l1-6zm5 1.5a2 2 0 1 0 0 4 2 2 0 0 0 0-4z"/></svg>
        714 555-0142
      </li>
      <li>
        <svg viewBox="0 0 16 16"><path d="M4 1h8v14H4V1zm1.5 1.5v10h5v-10h-5zM7 13h2v1H7z"/></svg>
        714 555-0142
      </li>
      <li>
        <svg viewBox="0 0 16 16"><path d="M1 3h14v10H1V3zm1.5 1.5v.4L8 9l5.5-4.1v-.4h-11zm0 2.3v4.7h11V6.8L8 10.9 2.5 6.8z"/></svg>
        info@raysfreshcrew.com
      </li>
      <li>
        <svg viewBox="0 0 16 16"><path d="M8 1a7 7 0 1 0 0 14A7 7 0 0 0 8 1zm0 1.5c.8 0 1.7 1.5 2 4H6c.3-2.5 1.2-4 2-4zM2.6 7h2c-.1.6 0 1.4 0 2h-2a5.5 5.5 0 0 1 0-2zm8.8 0h2a5.5 5.5 0 0 1 0 2h-2c0-.6.1-1.4 0-2zM6 9.5h4c-.3 2.5-1.2 4-2 4s-1.7-1.5-2-4z"/></svg>
        www.raysfreshcrew.com
      </li>
    </ul>

    <div class="address">
      418 Maple Grove Ave, #112<br>
      Lakewood, OH 44107
    </div>

    <svg class="footer-band" viewBox="0 0 700 110" preserveAspectRatio="none" aria-hidden="true">
      <polyline points="0,84 464,84 482,44 700,44" fill="none" stroke="#231f20" stroke-width="6"/>
      <polygon points="0,96 474,96 494,54 700,54 700,110 0,110" fill="#ec4a43"/>
    </svg>
    <div class="website-tag">www.raysfreshcrew.com</div>
  </section>

</body>
</html>
```